Business Card Design Project for Web Development Company

Need a professional card that stands out with both color and texture.
We provide websites and web development services for small businesses with a focus on connections. Examples include: Automotive repair shop, we take their repair logs and make them available online so their customers can view, print and share (when selling) their maintenance records. Vet clinic, we create systems where customers can sign up for a recurring payment program for the annual wellness checks on their pets and get reminders when it's time, then see and schedule their own appointments. Etc... So not simply a website, but one that connects systems or customers to the business.
Important - !!!!We will be using http://inkvaleprinters.com/ for the cards, so take a look at what options are available for business card printing, they can do a lot of cool things!!!!
You can pick any 1-3 options from inkvaleprinters. I'm leaning towards a black background, but the logo will work on any color.
Front:
Marcus Telford
2750 SW 8th Ave STE 214-587
Bend, OR 97701
541-617-2038 - cell
541-259-7306 - office
marcus@sitelinkhub.com
www.SiteLinkHub.com
Updates
We provide websites and web development services for small businesses with a focus on connections. Examples include: Automotive repair shop, we take their repair logs and make them available online so their customers can view, print and share (when selling) their maintenance records. Vet clinic, we create systems where customers can sign up for a recurring payment program for the annual wellness checks on their pets and get reminders when it''s time, then see and schedule their own appointments. Etc... So not simply a website, but one that connects systems or customers to the business.
Target Market(s)
Small business owners
Industry/Entity Type
Automotive
Look and feel
Each slider illustrates characteristics of the customer's brand and the style your logo design should communicate.

```html
<!DOCTYPE html>
<html lang="en">
<head>
<meta charset="utf-8">
<title>SiteLinkHub – Business Card</title>
<link rel="stylesheet" href="https://fonts.googleapis.com/css2?family=Bree+Serif&family=Courgette&family=Delius&family=Gelasio:wght@500&display=swap">
<style>
  :root {
    --card-black: #121416;
    --hex-grey: #2a2d31;
    --glow-cyan: #16b4dc;
    --band-cyan: #1fb7cf;
    --text-blue: #6eb6f2;
    --tagline-blue: #a9d4ff;
    --logo-blue: #3aaee0;
    --name-white: #ffffff;
    --shadow-black: #000000;
  }
  * { margin: 0; padding: 0; box-sizing: border-box; }
  html, body {
    width: 1200px; height: 746px; overflow: hidden;
    background: #ffffff;
  }
  .card {
    position: relative;
    width: 1200px; height: 746px;
    overflow: hidden;
    background: var(--card-black);
  }
  .card-texture {
    position: absolute; inset: 0;
    width: 100%; height: 100%;
  }
  .band {
    position: absolute; left: 0; width: 100%;
    background: var(--band-cyan);
  }
  .band-top { top: 0; height: 10px; }
  .band-bottom { bottom: 0; height: 14px; }

  .company-name {
    position: absolute; top: 42px; left: 0; width: 100%;
    text-align: center;
    font-family: "Bree Serif", serif;
    font-size: 104px; line-height: 1;
    color: var(--logo-blue);
  }

  .taglines {
    position: absolute; top: 204px; left: 0; width: 100%;
    text-align: center;
    font-family: "Courgette", cursive;
    font-size: 18px; line-height: 33px;
    color: var(--tagline-blue);
    text-shadow: 0 0 2px var(--shadow-black), 1px 1px 1px var(--shadow-black), -1px -1px 1px #2a5aa8;
  }

  .person-name {
    position: absolute; top: 378px; left: 90px;
    font-family: "Gelasio", serif; font-weight: 500;
    font-size: 54px; letter-spacing: 0.42em;
    color: var(--name-white);
    text-shadow: 0 0 3px var(--shadow-black), 2px 2px 3px var(--shadow-black), -2px -1px 2px var(--shadow-black);
  }

  .contact {
    position: absolute;
    color: var(--text-blue);
    text-shadow: 0 0 3px var(--shadow-black), 2px 2px 2px var(--shadow-black);
  }
  .address {
    top: 512px; left: 20px;
    font-family: "Bree Serif", serif;
    font-size: 33px; line-height: 43px;
  }
  .address .line-city { padding-left: 40px; }

  .phones {
    top: 492px; right: 24px;
    text-align: right;
    font-family: "Delius", cursive;
    font-size: 37px; line-height: 62px;
    letter-spacing: 0.04em;
  }
  .phones .line-office { margin-right: -10px; }

  .web-links {
    top: 622px; left: 0; width: 1096px;
    text-align: center;
    font-family: "Delius", cursive;
    font-size: 35px; line-height: 62px;
  }
</style>
</head>
<body>
  <main class="card">
    <svg class="card-texture" viewBox="0 0 1200 746" role="img" aria-label="Dark hexagon mesh texture lit by soft cyan glows">
      <defs>
        <radialGradient id="glow-center" cx="403" cy="428" r="170" gradientUnits="userSpaceOnUse">
          <stop offset="0" stop-color="var(--glow-cyan)" stop-opacity="0.75"/>
          <stop offset="0.35" stop-color="var(--glow-cyan)" stop-opacity="0.2"/>
          <stop offset="1" stop-color="var(--glow-cyan)" stop-opacity="0"/>
        </radialGradient>
        <radialGradient id="glow-upper" cx="800" cy="150" r="160" gradientUnits="userSpaceOnUse">
          <stop offset="0" stop-color="var(--glow-cyan)" stop-opacity="0.35"/>
          <stop offset="1" stop-color="var(--glow-cyan)" stop-opacity="0"/>
        </radialGradient>
        <radialGradient id="glow-corner-right" cx="1200" cy="350" r="220" gradientUnits="userSpaceOnUse">
          <stop offset="0" stop-color="var(--glow-cyan)" stop-opacity="0.35"/>
          <stop offset="1" stop-color="var(--glow-cyan)" stop-opacity="0"/>
        </radialGradient>
        <radialGradient id="glow-corner-left" cx="0" cy="680" r="240" gradientUnits="userSpaceOnUse">
          <stop offset="0" stop-color="var(--glow-cyan)" stop-opacity="0.3"/>
          <stop offset="1" stop-color="var(--glow-cyan)" stop-opacity="0"/>
        </radialGradient>
        <linearGradient id="mesh-tone" x1="0" y1="0" x2="0" y2="1">
          <stop offset="0" stop-color="var(--card-black)"/>
          <stop offset="0.5" stop-color="var(--hex-grey)"/>
          <stop offset="1" stop-color="var(--card-black)"/>
        </linearGradient>
      </defs>
      <rect width="1200" height="746" fill="url(#mesh-tone)"/>
      <rect width="1200" height="746" fill="url(#glow-upper)"/>
      <rect width="1200" height="746" fill="url(#glow-corner-right)"/>
      <rect width="1200" height="746" fill="url(#glow-corner-left)"/>
      <rect width="1200" height="746" fill="url(#glow-center)"/>
    </svg>

    <div class="band band-top"></div>
    <div class="band band-bottom"></div>

    <h1 class="company-name">SiteLinkHub</h1>

    <div class="taglines">
      <p>websites</p>
      <p>web development services</p>
      <p>not simply a website, but one that connects systems or customers to the business.</p>
    </div>

    <h2 class="person-name">Marcus Telford</h2>

    <address class="contact address">
      <div class="line-street">2750 SW 8th Ave STE 214-587</div>
      <div class="line-city">Bend, OR 97701</div>
    </address>

    <div class="contact phones">
      <div class="line-cell">541-617-2038 - cell</div>
      <div class="line-office">541-259-7306 - office</div>
    </div>

    <div class="contact web-links">
      <div class="line-email">marcus@sitelinkhub.com</div>
      <div class="line-site">www.SiteLinkHub.com</div>
    </div>
  </main>
</body>
</html>
```